Property investment company needs a letterhead design!

We are a new residential and commercial property investment company. Name of the company is Morvesta Group, LLC. We have a new logo and now we need letterhead! We prefer to have a professional and upscale appearance. We don't have any fixed requirements, so be creative! Thank you for considering this project. We are so excited to see what happens!

Target Market(s)

Professional

Industry/Entity Type

Real Estate Development

```html
<!DOCTYPE html>
<html lang="en">
<head>
<meta charset="utf-8">
<title>Morvesta Group, LLC — Letterhead</title>
<link rel="stylesheet" href="https://fonts.googleapis.com/css2?family=Open+Sans:wght@400;600;700&family=Questrial&display=swap">
<style>
  :root {
    --navy: #0f2340;
    --ink: #1d2a3e;
    --muted: #3a3f47;
    --mist: #f1f1f1;
    --paper: #ffffff;
  }
  * { margin: 0; padding: 0; box-sizing: border-box; }
  html, body { width: 848px; height: 1200px; overflow: hidden; background: var(--paper); }
  .letterhead {
    position: relative; width: 848px; height: 1200px; overflow: hidden;
    background: var(--paper); font-family: "Open Sans", sans-serif; color: var(--ink);
  }
  .backdrop {
    position: absolute; left: 0; top: 975px; width: 455px; height: 225px;
    background: linear-gradient(180deg, rgba(241,241,241,0) 0%, var(--mist) 60%, var(--mist) 100%);
  }
  .date { position: absolute; left: 99px; top: 101px; font-size: 14.6px; color: var(--muted); }
  .company { position: absolute; left: 96px; top: 152px; font-size: 22px; font-weight: 600; color: var(--navy); letter-spacing: 0.2px; }
  .contact { position: absolute; left: 96px; top: 203px; font-size: 14px; color: var(--ink); line-height: 22.3px; }
  .contact b { display: inline-block; width: 24px; font-weight: 700; }
  .brand {
    position: absolute; right: 83px; top: 208px;
    display: flex; align-items: center; gap: 8px; white-space: nowrap;
    font-size: 16px; font-weight: 700; color: var(--navy); line-height: 1.2;
  }
  .brand-dot { width: 22px; height: 22px; border-radius: 50%; background: var(--navy); flex: none; }
  .salutation { position: absolute; left: 95px; top: 328px; font-size: 15px; font-weight: 600; color: var(--navy); }
  .body { position: absolute; left: 95px; width: 670px; font-size: 13.4px; line-height: 22px; color: var(--ink); }
  .body .line { display: block; white-space: nowrap; text-align: justify; text-align-last: justify; }
  .body .line.end { text-align-last: left; }
  .p1 { top: 388px; } .p2 { top: 521px; } .p3 { top: 676px; } .p4 { top: 755px; left: 98px; width: 662px; }
  .signature { position: absolute; left: 96px; top: 930px; width: 172px; height: 30px; background: linear-gradient(90deg, #e4e6ea, #d6d9df); border-radius: 4px; }
  .signer { position: absolute; left: 145px; top: 974px; line-height: 16px; }
  .signer-name { font-size: 14px; font-weight: 700; color: var(--ink); }
  .signer-role { font-size: 13.5px; color: var(--muted); }
  .footer-contact { position: absolute; left: 573px; top: 935px; font-family: "Questrial", sans-serif; color: var(--muted); }
  .footer-row { display: flex; align-items: flex-start; gap: 23px; height: 43.5px; }
  .footer-icon { width: 27px; height: 27px; background: var(--navy); display: flex; align-items: center; justify-content: center; flex: none; margin-top: 1px; }
  .footer-text { font-size: 14.6px; line-height: 16px; }
</style>
</head>
<body>
<main class="letterhead">
  <div class="backdrop" role="img" aria-label="Faint grey landscape backdrop area"></div>

  <p class="date">Date, 10 September, 2019</p>
  <h1 class="company">MORVESTA GROUP,LLC</h1>
  <div class="contact">
    <div><b>A :</b>2280 Wrenfield Ct</div>
    <div><b>W :</b>www.morvestaweb.com</div>
    <div><b>P :</b>+880 - 54321 - 9876</div>
  </div>

  <div class="brand"><span class="brand-dot"></span><span>Morvesta Group, LLC</span></div>

  <p class="salutation">Dear Mr, Ellis</p>

  <p class="body p1">
    <span class="line">lhis is a sample letter that has been placed to demonstrate typing remat (Your Company). letterheadikk</span>
    <span class="line">lesign. When positioned properly, it will serve to work in harmony with all other elements letterheadasr</span>
    <span class="line">lhis letterhead design is meant to project an image we have created pacious feelinguggest rengththelki</span>
    <span class="line">Lpaciousnes contributes h we have created a very spacious feeling. The simplicity suggest engththekuk</span>
    <span class="line">Nesthetics the layout. These basic qualities along with the aesthetics the layout. These basic qualities ai</span>
  </p>
  <p class="body p2">
    <span class="line">Lhis letterhead design is meant project an image of professionalism reliability. By using simple aligengk</span>
    <span class="line">Le have created a very spacious feeling. The simplicity suggest rengththe spaciousnes contributes hktr</span>
    <span class="line end">lesthetics the layout. These basic qualities along with the (Your Company)</span>
    <span class="line">lok and helps reinforce the (Your Company) brand. letterhead design is meant to project an image prei</span>
    <span class="line">lesign. When positioned properly, it will serve to work in harmony all the other elements letterhead.aai</span>
    <span class="line end">Fionalism and reliability.</span>
  </p>
  <p class="body p3">
    <span class="line">This letterhead design is based on the (Form of your logo) form (Your Company) logo. Each stationeryet</span>
    <span class="line">We have created a very spacious feeling. The simplicity suggests strength the spaciousnes contributesir</span>
    <span class="line end">Prt of the (Form of your logo).</span>
  </p>
  <p class="body p4">
    <span class="line">Design. When positioned properly, it will serve to work in harmony all the other elements letterhead.a</span>
    <span class="line end">sionalism and reliability.</span>
  </p>

  <div class="signature" role="img" aria-label="Handwritten signature of Daniel Harrow"></div>
  <div class="signer">
    <div class="signer-name">Daniel Harrow</div>
    <div class="signer-role">Manager</div>
  </div>

  <div class="footer-contact">
    <div class="footer-row">
      <span class="footer-icon">
        <svg width="15" height="13" viewBox="0 0 15 13" aria-hidden="true"><path d="M1 4 Q7.5 -1 14 4 L12 5.5 L10 4 L5 4 L3 5.5 Z M3 6 H12 L13 12 H2 Z" fill="#fff"/><circle cx="7.5" cy="9" r="1.8" fill="#0f2340"/></svg>
      </span>
      <div class="footer-text">+000 55510 2468<br>+000 55510 2468</div>
    </div>
    <div class="footer-row">
      <span class="footer-icon">
        <svg width="15" height="15" viewBox="0 0 15 15" aria-hidden="true"><circle cx="7.5" cy="7.5" r="6" fill="none" stroke="#fff" stroke-width="1.3"/><path d="M1.5 7.5 H13.5 M7.5 1.5 Q4 7.5 7.5 13.5 M7.5 1.5 Q11 7.5 7.5 13.5" fill="none" stroke="#fff" stroke-width="1"/></svg>
      </span>
      <div class="footer-text">morvestasite.com<br>hello@morvestamail.com</div>
    </div>
    <div class="footer-row">
      <span class="footer-icon">
        <svg width="12" height="16" viewBox="0 0 12 16" aria-hidden="true"><path d="M6 0 A6 6 0 0 1 12 6 C12 10 6 16 6 16 C6 16 0 10 0 6 A6 6 0 0 1 6 0 Z" fill="#fff"/><circle cx="6" cy="6" r="2.2" fill="#0f2340"/></svg>
      </span>
      <div class="footer-text">Street Address Here<br>Singapore, 2222</div>
    </div>
  </div>
</main>
</body>
</html>
```